Breezeline Climate Crew WA Truck

I want a truck desing that screams Professional, Friendly and serious about work. you can find some of our work on our website, facebook and instagram.
https://breezelinecrew.example.com.au/
https://www.instagram.com/bzcrewox/
https://www.facebook.com/profile.php?id=70318825094631

The design needs to include our refrigeration license: AU38452 and electrical License: EC94031
I want the colours to be consistent with my Logo.

Key Notes to be included in the design, I want to let people know we do the following;
- Commercial and Residential
- Repairs, Service and Installation
- Reverse cycle ducted Air Conditioning
- Wall Split Air Conditioning
- Ceiling Cassettes
- Evaporative Air Conditioning
- Cool Rooms
- Display Fridges
- Beer Chillers

```html
<!DOCTYPE html>
<html lang="en">
<head>
<meta charset="utf-8">
<title>Breezeline Climate Crew WA – Truck Wrap</title>
<link href="https://fonts.googleapis.com/css2?family=Oswald:wght@400;500;700&display=swap" rel="stylesheet">
<style>
  :root{
    --orange:#f07a1a;
    --orange-light:#f9a23c;
    --blue:#1f86c8;
    --navy:#1d3f73;
    --white:#ffffff;
    --ink:#1d3f73;
    --bg:#e9edf1;
    --frame:#c9ced4;
  }
  *{margin:0;padding:0;box-sizing:border-box}
  html,body{width:1200px;height:1200px;overflow:hidden;background:var(--bg)}
  .canvas{position:relative;width:1200px;height:1200px}
  .wrap-panel{
    position:absolute;left:50px;width:1100px;height:520px;
    background:var(--white);border:6px solid var(--frame);overflow:hidden;
    font-family:'Oswald',sans-serif;
  }
  .wrap-panel--a{top:50px}
  .wrap-panel--b{top:630px}
  .wrap-panel svg.art{position:absolute;inset:0;width:100%;height:100%}
  .service-list{position:absolute;list-style:none;font-weight:500;font-size:19px;line-height:29px;text-transform:uppercase}
  .service-list li::before{content:"";display:inline-block;width:7px;height:7px;border-radius:50%;margin-right:8px;vertical-align:middle}
  .service-list .indent{padding-left:15px}
  .service-list .indent::before{display:none}
  .wrap-panel--a .service-list{left:70px;top:24px;color:var(--white);width:340px}
  .wrap-panel--a .service-list li::before{background:var(--navy)}
  .wrap-panel--b .service-list{left:690px;top:16px;color:var(--ink);width:380px}
  .wrap-panel--b .service-list li::before{background:var(--orange)}
  .brand{position:absolute;text-align:center;color:var(--orange);font-weight:700;text-transform:uppercase;line-height:1;white-space:nowrap}
  .brand__mark{display:block;width:64px;height:64px;border-radius:50%;background:var(--orange);margin:0 auto 12px}
  .brand__name{display:block;font-size:36px;letter-spacing:1px}
  .brand__sub{display:block;font-size:22px;letter-spacing:4px;margin-top:6px}
  .wrap-panel--a .brand{left:580px;top:40px;width:460px}
  .wrap-panel--b .brand{left:110px;top:50px;width:500px}
  .wrap-panel--b .brand__name{font-size:40px}
  .licence{position:absolute;left:28px;color:var(--white);font-size:21px;font-weight:500;line-height:26px}
  .wrap-panel--a .licence{top:418px}
  .wrap-panel--b .licence{top:406px}
  .contact{position:absolute;color:var(--white)}
  .contact__row{display:flex;align-items:center;gap:10px}
  .social-dot{width:30px;height:30px;border-radius:50%;background:var(--white)}
  .contact__phone{font-size:50px;font-weight:500;margin-left:10px;letter-spacing:1px;line-height:1.2}
  .contact__web{font-size:20px;font-weight:500;color:var(--navy);margin-top:2px}
  .wrap-panel--a .contact{left:230px;top:395px}
  .wrap-panel--a .contact__web{margin-left:110px}
  .wrap-panel--b .contact{left:640px;top:385px}
  .wrap-panel--b .social-dot{background:var(--navy)}
  .wrap-panel--b .contact__web{margin-left:110px}
</style>
</head>
<body>
<main class="canvas">

  <section class="wrap-panel wrap-panel--a" aria-label="Truck box side wrap, option one">
    <svg class="art" viewBox="0 0 1100 520" preserveAspectRatio="none" aria-hidden="true">
      <defs>
        <linearGradient id="orangeA" x1="0" y1="0" x2="1" y2="1">
          <stop offset="0" stop-color="#ee6f16"/><stop offset="1" stop-color="#f9a23c"/>
        </linearGradient>
      </defs>
      <path d="M0,0 L340,0 C420,150 500,240 660,275 C820,305 960,320 1100,330 L1100,520 L0,520 Z" fill="url(#orangeA)"/>
      <path d="M352,0 C432,150 512,232 668,262 C826,292 964,306 1100,314" fill="none" stroke="var(--blue)" stroke-width="14"/>
      <path d="M520,360 C640,310 760,300 900,330 C980,345 1040,355 1100,356" fill="none" stroke="var(--blue)" stroke-width="5"/>
      <path d="M0,370 C110,390 210,440 310,520 L0,520 Z" fill="var(--navy)"/>
      <path d="M0,362 C115,382 218,432 322,520" fill="none" stroke="var(--white)" stroke-width="5"/>
    </svg>
    <ul class="service-list">
      <li>Wall Split Air Conditioning</li>
      <li>Ceiling Cassettes</li>
      <li>Evaporative Air Conditioning</li>
      <li>Cool Rooms</li>
      <li>Display Fridges</li>
      <li>Beer Chillers</li>
      <li>Commercial and Residential</li>
      <li>Repairs, Service and Installation</li>
      <li>Reverse Cycle Ducted Air</li>
      <li class="indent">Conditioning</li>
    </ul>
    <div class="brand">
      <span class="brand__mark"></span>
      <span class="brand__name">Breezeline Climate Crew</span>
      <span class="brand__sub">WA</span>
    </div>
    <p class="licence">AU38452<br>LIC# EC94031</p>
    <div class="contact">
      <div class="contact__row"><span class="social-dot"></span><span class="social-dot"></span><span class="contact__phone">(870) 555-0148</span></div>
      <p class="contact__web">www.breezelinecrew.example.com.au</p>
    </div>
  </section>

  <section class="wrap-panel wrap-panel--b" aria-label="Truck box side wrap, option two">
    <svg class="art" viewBox="0 0 1100 520" preserveAspectRatio="none" aria-hidden="true">
      <defs>
        <linearGradient id="orangeB" x1="0" y1="0" x2="1" y2="0">
          <stop offset="0" stop-color="#f9a23c"/><stop offset="1" stop-color="#ee6f16"/>
        </linearGradient>
      </defs>
      <path d="M0,210 C180,260 360,340 600,345 C800,345 960,305 1100,250 L1100,520 L0,520 Z" fill="url(#orangeB)"/>
      <path d="M420,318 C520,338 620,342 720,336 C860,325 980,290 1100,240" fill="none" stroke="var(--blue)" stroke-width="14"/>
      <path d="M0,360 C110,380 200,440 290,520 L0,520 Z" fill="var(--navy)"/>
      <path d="M0,352 C115,372 208,432 302,520" fill="none" stroke="var(--white)" stroke-width="5"/>
    </svg>
    <div class="brand">
      <span class="brand__mark"></span>
      <span class="brand__name">Breezeline Climate Crew</span>
      <span class="brand__sub">WA</span>
    </div>
    <ul class="service-list">
      <li>Wall Split Air Conditioning</li>
      <li>Ceiling Cassettes</li>
      <li>Evaporative Air Conditioning</li>
      <li>Cool Rooms</li>
      <li>Display Fridges</li>
      <li>Beer Chillers</li>
      <li>Commercial and Residential</li>
      <li>Repairs, Service and Installation</li>
      <li>Reverse Cycle Ducted Air</li>
      <li class="indent">Conditioning</li>
    </ul>
    <p class="licence">AU38452<br>LIC# EC94031</p>
    <div class="contact">
      <div class="contact__row"><span class="social-dot"></span><span class="social-dot"></span><span class="contact__phone">(870) 555-0148</span></div>
      <p class="contact__web">www.breezelinecrew.example.com.au</p>
    </div>
  </section>

</main>
</body>
</html>
```